QTR business cards

I need a Business card design for my self. I am behavior analyst owner of a new company based in Miami. We offer Applied Behavior Analysis (ABA) services to individuals with developmental disabilities.

Business

```html
<!DOCTYPE html>
<html lang="en">
<head>
<meta charset="utf-8">
<title>QTR Business Cards</title>
<link href="https://fonts.googleapis.com/css2?family=Cinzel:wght@400;600&family=Open+Sans:wght@400&display=swap" rel="stylesheet">
<style>
  :root {
    --page-bg: #ececec;
    --card-white: #ffffff;
    --brand-blue: #1a5ea8;
    --brand-blue-deep: #0c4588;
    --brand-blue-light: #2a7cc6;
    --brand-green: #4ea843;
    --text-dark: #333a44;
    --rule-grey: #c9ccd1;
  }
  * { box-sizing: border-box; margin: 0; padding: 0; }
  html, body { width: 1200px; height: 1024px; overflow: hidden; }
  body {
    background: var(--page-bg);
    display: flex;
    flex-direction: column;
    align-items: center;
    justify-content: center;
    gap: 30px;
  }
  .card {
    position: relative;
    width: 820px;
    height: 469px;
    overflow: hidden;
    box-shadow: 0 6px 18px rgba(0,0,0,0.18);
  }

  /* Front */
  .card-front { background: var(--card-white); }
  .card-front .wave { position: absolute; inset: 0; width: 100%; height: 100%; }
  .brand-block {
    position: absolute;
    left: 70px;
    top: 150px;
    display: flex;
    align-items: center;
    gap: 18px;
  }
  .brand-dot {
    width: 26px; height: 26px; border-radius: 50%;
    background: var(--brand-green);
  }
  .brand-name {
    font-family: "Cinzel", serif;
    font-weight: 600;
    font-size: 92px;
    letter-spacing: 4px;
    color: var(--brand-blue);
    line-height: 1;
  }
  .divider {
    position: absolute;
    left: 395px;
    top: 70px;
    width: 1px;
    height: 250px;
    background: var(--rule-grey);
  }
  .contact {
    position: absolute;
    left: 430px;
    top: 70px;
    font-family: "Open Sans", sans-serif;
    color: var(--text-dark);
  }
  .contact-name {
    font-family: "Cinzel", serif;
    font-size: 25px;
    color: var(--brand-blue);
    letter-spacing: 1px;
  }
  .contact-title {
    font-family: "Cinzel", serif;
    font-size: 15px;
    color: var(--text-dark);
    margin-bottom: 26px;
  }
  .contact-list { list-style: none; }
  .contact-list li {
    display: flex;
    align-items: flex-start;
    gap: 12px;
    font-size: 14px;
    line-height: 1.45;
    margin-bottom: 10px;
  }
  .contact-list svg { width: 14px; height: 14px; flex: none; margin-top: 3px; fill: var(--brand-blue-deep); }

  /* Back */
  .card-back {
    background: radial-gradient(ellipse at 45% 45%, var(--brand-blue-light) 0%, var(--brand-blue) 55%, var(--brand-blue-deep) 100%);
    display: flex;
    align-items: center;
    justify-content: center;
  }
  .card-back .brand-name {
    color: var(--card-white);
    font-size: 120px;
    letter-spacing: 8px;
  }
</style>
</head>
<body>

  <section class="card card-front">
    <svg class="wave" viewBox="0 0 820 469" preserveAspectRatio="none" aria-hidden="true">
      <path d="M560,352 C680,300 770,230 820,140 L820,170 C770,255 680,320 560,362 Z" fill="var(--brand-green)"/>
      <path d="M0,469 L0,410 C240,440 540,400 700,300 C760,262 800,220 820,180 L820,469 Z" fill="var(--brand-blue)"/>
    </svg>

    <div class="brand-block">
      <span class="brand-dot"></span>
      <span class="brand-name">QTR</span>
    </div>

    <div class="divider"></div>

    <div class="contact">
      <p class="contact-name">Daniel R. Ortega</p>
      <p class="contact-title">Managing Member,</p>
      <ul class="contact-list">
        <li>
          <svg viewBox="0 0 24 24"><path d="M6.6 10.8a15.1 15.1 0 0 0 6.6 6.6l2.2-2.2c.3-.3.7-.4 1-.2 1.1.4 2.3.6 3.6.6.6 0 1 .4 1 1V20c0 .6-.4 1-1 1A17 17 0 0 1 3 4c0-.6.4-1 1-1h3.5c.6 0 1 .4 1 1 0 1.3.2 2.5.6 3.6.1.3 0 .7-.2 1z"/></svg>
          (305) 555-0142,
        </li>
        <li>
          <svg viewBox="0 0 24 24"><path d="M6 3h10v5H6zM4 9h16a2 2 0 0 1 2 2v7h-4v3H6v-3H2v-7a2 2 0 0 1 2-2zm4 7v3h8v-3z"/></svg>
          (305) 555-0178,
        </li>
        <li>
          <svg viewBox="0 0 24 24"><path d="M2 5h20v14H2zm2 2v.5l8 5 8-5V7l-8 5z"/></svg>
          daniel@qtrbehavior.com
        </li>
        <li>
          <svg viewBox="0 0 24 24"><path d="M12 2a7 7 0 0 0-7 7c0 5 7 13 7 13s7-8 7-13a7 7 0 0 0-7-7zm0 9.5A2.5 2.5 0 1 1 12 6.5a2.5 2.5 0 0 1 0 5z"/></svg>
          <span>2250 Harbor Lane, Miami,<br>FL 33131,</span>
        </li>
      </ul>
    </div>
  </section>

  <section class="card card-back">
    <span class="brand-name">QTR</span>
  </section>

</body>
</html>
```